Owner of Clinical Testing Lab/. Pixel Harbor Logo completed. Need Matching business Cards

Im the owner of and need cards for business. Colors fonts and logo already purchased through pixel harbor and have the source files. Like to keep same color format , Include logo one side. My Name Address of Lab. My cell number, Lab telephone number and website address. Want to keep simple.

Target Market(s)

Customers

Industry/Entity Type

HealthCare

Contact Information for Business Card

Dr. Corisande Threlkeld Ph.D. Address: QVT Foundry Campus 4417 Foundry Campus Loop Building 2600 Room 314. Marlow Bend KS 70931. Phone : 555.317.0942

Requirements
Must have
• Logo - Color same

```html
<!DOCTYPE html>
<html lang="en">
<head>
<meta charset="utf-8">
<title>Meridian Assay Labs — Business Cards</title>
<link href="https://fonts.googleapis.com/css2?family=Mulish:wght@400;700&display=swap" rel="stylesheet">
<style>
  :root {
    --backdrop: #d8d8d8;
    --card: #ffffff;
    --navy: #1f4f8e;
    --teal: #5cc5ad;
    --shadow: rgba(0, 0, 0, 0.18);
  }
  * { box-sizing: border-box; margin: 0; padding: 0; }
  html, body { width: 1200px; height: 800px; overflow: hidden; }
  body {
    background: var(--backdrop);
    font-family: "Mulish", "Century Gothic", sans-serif;
    color: var(--navy);
    position: relative;
  }
  .card {
    position: absolute;
    width: 540px;
    height: 309px;
    background: var(--card);
    box-shadow: 0 10px 24px var(--shadow);
    overflow: hidden;
  }
  .card--front { left: 40px; top: 246px; }
  .card--back { left: 620px; top: 246px; }

  /* wordmark */
  .wordmark {
    position: absolute;
    display: flex;
    align-items: center;
    gap: 10px;
    font-weight: 400;
    color: var(--navy);
    letter-spacing: 0.02em;
    line-height: 1.05;
  }
  .wordmark__dot {
    width: 16px; height: 16px;
    border-radius: 50%;
    background: var(--teal);
    flex: none;
  }
  .card--front .wordmark { left: 36px; top: 74px; font-size: 27px; width: 210px; }
  .card--back .wordmark { left: 50%; top: 112px; transform: translateX(-50%); font-size: 32px; white-space: nowrap; }

  /* front rules */
  .rule { position: absolute; height: 1px; }
  .rule--teal { background: var(--teal); left: 0; top: 248px; width: 196px; }
  .rule--navy { background: var(--navy); left: 256px; top: 278px; width: 284px; }
  .helix-ornament {
    position: absolute;
    left: 202px; top: 240px;
    width: 48px; height: 46px;
    border-radius: 50%;
    background: linear-gradient(160deg, rgba(92,197,173,0.55), rgba(31,79,142,0.55));
  }
  .divider {
    position: absolute;
    left: 250px; top: 36px;
    width: 1px; height: 178px;
    background: var(--teal);
  }

  /* contact block */
  .contact {
    position: absolute;
    left: 272px; top: 36px;
    width: 250px;
  }
  .contact__name { font-weight: 700; font-size: 15.5px; margin-bottom: 6px; }
  .contact__address {
    font-style: normal;
    font-size: 12.5px;
    line-height: 1.38;
    margin-bottom: 6px;
  }
  .contact__list { list-style: none; font-size: 12.5px; line-height: 1.45; }
  .contact__list li { display: flex; align-items: center; gap: 7px; }
  .icon {
    width: 14px; height: 14px;
    border-radius: 50%;
    background: var(--teal);
    display: inline-flex; align-items: center; justify-content: center;
    flex: none;
  }
  .icon svg { width: 9px; height: 9px; }

  .website {
    position: absolute;
    left: 0; right: 0; top: 192px;
    text-align: center;
    font-size: 13.5px;
    color: var(--navy);
  }
</style>
</head>
<body>

<section class="card card--front" aria-label="Business card front">
  <div class="wordmark"><span class="wordmark__dot"></span><span>Meridian Assay Labs</span></div>
  <div class="divider"></div>
  <div class="rule rule--teal"></div>
  <div class="helix-ornament" role="img" aria-label="Small helix ornament in teal and navy"></div>
  <div class="rule rule--navy"></div>

  <div class="contact">
    <p class="contact__name">Dr. Corisande Threlkeld Ph.D.</p>
    <address class="contact__address">
      QVT Foundry Campus 4417<br>
      Foundry Campus Loop<br>
      Building 2600 Room 314.<br>
      Marlow Bend KS 70931.
    </address>
    <ul class="contact__list">
      <li><span class="icon"><svg viewBox="0 0 10 10"><path d="M2 1.2l1.6-.2.8 2-1 .8c.5 1.1 1.3 1.9 2.4 2.4l.8-1 2 .8-.2 1.6C6 8 2 4 2 1.2z" fill="#fff"/></svg></span>Lab : 555.317.0942</li>
      <li><span class="icon"><svg viewBox="0 0 10 10"><rect x="3" y="1" width="4" height="8" rx="0.8" fill="none" stroke="#fff" stroke-width="1"/><circle cx="5" cy="7.6" r="0.5" fill="#fff"/></svg></span>555.317.0942</li>
      <li><span class="icon"><svg viewBox="0 0 10 10"><rect x="1.5" y="2.5" width="7" height="5" fill="none" stroke="#fff" stroke-width="1"/><path d="M1.5 2.5l3.5 3 3.5-3" fill="none" stroke="#fff" stroke-width="1"/></svg></span>info@meridianassaylabs.com</li>
      <li><span class="icon"><svg viewBox="0 0 10 10"><circle cx="5" cy="5" r="3.6" fill="none" stroke="#fff" stroke-width="0.9"/><path d="M1.4 5h7.2M5 1.4c-1.6 2-1.6 5.2 0 7.2M5 1.4c1.6 2 1.6 5.2 0 7.2" fill="none" stroke="#fff" stroke-width="0.8"/></svg></span>www.meridianassaylabs.com</li>
    </ul>
  </div>
</section>

<section class="card card--back" aria-label="Business card back">
  <div class="wordmark"><span class="wordmark__dot"></span><span>Meridian Assay Labs</span></div>
  <p class="website">www.meridianassaylabs.com</p>
</section>

</body>
</html>
```